Natural deodorant label

Natural clean deodorant line. Need modernize label which can be sized for both the regular and travel size deodorants. 2.75 x 3" and 1x2". Important to highlight no baking soda and its natural. Also has no aluminum, preservatives, nor chemicals. Its gender inclusive and safe for all ages. Please see website at www.lorvatique.com. will attach current label. Will need a label that i would be able to update with new scents as they come. Want a clean look.
Updates

Need extra days to review

Target Market(s)

the working mother/wife that lives a clean healthy life and pushes that for her family

Industry/Entity Type

health and beauty/deodorant/natural

Colors

Designer to choose colors to be used in the design.

Requirements
Must have
• No baking soda and gender inclusive on label. Clean look. Very little to no picture art.
Nice to have
• Potentially a different color representing the different scents. A brief description of the deodorant scent underneath the scent name. This can be found under the drop down menu titled valdora deodorant scents on the website www.lorvatique.com. Area on front label for a small barcode.
Should not have
• misspelled words; dark label

```html
<!DOCTYPE html>
<html lang="en">
<head>
<meta charset="utf-8">
<title>Valdora Deodorant Labels</title>
<link rel="stylesheet" href="https://fonts.googleapis.com/css2?family=Antonio:wght@300;400&family=Cinzel:wght@500&family=Great+Vibes&family=Poppins:wght@400;500;600&display=swap">
<style>
  :root {
    --ink: #111111;
    --paper: #ffffff;
    --stage: #b3b3b3;
    --page: #ffffff;
    --shadow: rgba(60, 70, 100, 0.22);
    --back-title: #2a140f;
    --yellow: #d9b814;  --yellow-wash: #f3ec9c;
    --sand: #b89a63;    --sand-wash: #ecd2bd;
    --gold: #8f6a1c;    --gold-wash: #dccb9c;
    --grey: #6b6b6b;    --grey-wash: #cfcfcf;
    --teal: #1a9a6c;    --teal-wash: #9fdcc6;
    --violet: #8a1fb5;  --violet-wash: #d3b2e8;
    --orange: #e0631c;  --orange-wash: #f7c08f;
    --blue: #1a7fbd;    --blue-wash: #a8d3e6;
  }
  * { box-sizing: border-box; margin: 0; padding: 0; }
  html, body { width: 1200px; height: 2400px; overflow: hidden; background: var(--page); }
  body { position: relative; font-family: "Poppins", sans-serif; color: var(--ink); }

  .stage { position: absolute; left: 0; top: 0; width: 1200px; height: 930px; background: var(--stage); }
  .stage .label { position: absolute; top: 237px; transform: scale(1.2); transform-origin: top left; }
  .stage .label:nth-child(1) { left: 155px; }
  .stage .label:nth-child(2) { left: 625px; }

  .label-sheet { position: absolute; left: 45px; top: 1010px; width: 1110px;
    display: grid; grid-template-columns: repeat(3, 350px); grid-auto-rows: 380px; gap: 40px 30px; }

  .label { --accent: var(--ink); --wash: var(--grey-wash);
    position: relative; width: 350px; height: 380px; background: var(--paper);
    box-shadow: 0 2px 10px var(--shadow); overflow: hidden;
    display: flex; flex-direction: column; align-items: center; text-align: center; }
  .label .wash { position: absolute; inset: 0;
    background:
      radial-gradient(ellipse 60% 45% at 20% 88%, var(--wash) 0%, transparent 70%),
      radial-gradient(ellipse 55% 40% at 85% 40%, var(--wash) 0%, transparent 70%),
      radial-gradient(ellipse 70% 50% at 60% 75%, var(--wash) 0%, transparent 75%),
      linear-gradient(to bottom, transparent 30%, color-mix(in srgb, var(--wash) 45%, transparent) 100%);
    opacity: 0.85; }
  .label > *:not(.wash) { position: relative; }

  .brand { margin-top: 20px; display: flex; flex-direction: column; align-items: center; }
  .brand-dot { width: 30px; height: 30px; border-radius: 50%; background: var(--ink); }
  .brand-name { margin-top: 8px; font-family: "Cinzel", serif; font-weight: 500; font-size: 15px; letter-spacing: 0.5px; }

  .product { margin-top: 6px; font-family: "Antonio", sans-serif; font-weight: 300; font-size: 74px; line-height: 0.95; letter-spacing: 2px; }
  .scent { margin-top: -6px; font-family: "Great Vibes", cursive; font-size: 38px; line-height: 1.05; color: var(--accent); white-space: nowrap; }
  .scent-note { margin-top: 8px; width: 250px; font-size: 10.5px; line-height: 1.25; font-weight: 500; }
  .divider { margin: 12px 0 11px; width: 18px; height: 2px; background: var(--accent); }
  .claims { font-size: 11px; line-height: 1.35; text-transform: uppercase; }
  .weight { margin-top: 4px; font-size: 9px; }
  .site { margin-top: 10px; font-size: 9.5px; font-weight: 600; letter-spacing: 3.2px; }

  .scent-coastal  { --accent: var(--yellow); --wash: var(--yellow-wash); }
  .scent-lagoon   { --accent: var(--sand);   --wash: var(--sand-wash); }
  .scent-velvet   { --accent: var(--gold);   --wash: var(--gold-wash); }
  .scent-unscented{ --accent: var(--grey);   --wash: var(--grey-wash); }
  .scent-amber    { --accent: var(--teal);   --wash: var(--teal-wash); }
  .scent-meadow   { --accent: var(--violet); --wash: var(--violet-wash); }
  .scent-orchard  { --accent: var(--orange); --wash: var(--orange-wash); }
  .scent-garden   { --accent: var(--blue);   --wash: var(--blue-wash); }

  .label-back .brand { margin-top: 32px; }
  .label-back .brand-dot { width: 24px; height: 24px; }
  .label-back .brand-name { font-size: 12px; }
  .label-back .product { margin-top: 14px; font-size: 50px; }
  .organic { margin-top: 6px; font-size: 14px; font-weight: 600; color: #4a4a4a; }
  .organic-sub { font-size: 9.5px; color: #4a4a4a; }
  .ingredients { margin-top: 14px; width: 210px; font-size: 9.5px; line-height: 1.3; }
  .ingredients strong { font-weight: 600; }
  .badges { margin-top: 16px; display: flex; gap: 16px; align-items: center; font-size: 10px; }
  .badge { display: flex; align-items: center; gap: 6px; }
  .badge svg { width: 24px; height: 24px; }
  .label-back .site { margin-top: 16px; }

  .sheet-caption { position: absolute; left: 805px; top: 2262px; width: 350px; text-align: center;
    font-family: "Poppins", sans-serif; font-weight: 600; font-size: 24px; color: var(--back-title); letter-spacing: 1px; }
</style>
</head>
<body>

<section class="stage">
  <article class="label scent-amber">
    <div class="wash" role="img" aria-label="Soft teal watercolour wash"></div>
    <div class="brand"><span class="brand-dot"></span><span class="brand-name">Lorvatique</span></div>
    <h2 class="product">VALDORA</h2>
    <p class="scent">Amber Dusk</p>
    <p class="scent-note">Warm, exotic scent with amber and sandalwood notes</p>
    <span class="divider"></span>
    <p class="claims">Naturally Refreshing<br>Baking Soda Free</p>
    <p class="weight">net wt. 2.5oz (70g)</p>
    <p class="site">www.lorvatique.com</p>
  </article>
  <article class="label scent-meadow">
    <div class="wash" role="img" aria-label="Soft lavender watercolour wash"></div>
    <div class="brand"><span class="brand-dot"></span><span class="brand-name">Lorvatique</span></div>
    <h2 class="product">VALDORA</h2>
    <p class="scent">Calm Meadow</p>
    <p class="scent-note">Calm, refreshing scent with lavender notes</p>
    <span class="divider"></span>
    <p class="claims">Naturally Refreshing<br>Baking Soda Free</p>
    <p class="weight">net wt. 2.5oz (70g)</p>
    <p class="site">www.lorvatique.com</p>
  </article>
</section>

<section class="label-sheet">
  <article class="label scent-coastal">
    <div class="wash" role="img" aria-label="Soft yellow watercolour wash"></div>
    <div class="brand"><span class="brand-dot"></span><span class="brand-name">Lorvatique</span></div>
    <h2 class="product">VALDORA</h2>
    <p class="scent">Coastal Drift</p>
    <p class="scent-note">Fresh, clean coconut scent with vanilla bean and pineapple notes</p>
    <span class="divider"></span>
    <p class="claims">Naturally Refreshing<br>Baking Soda Free</p>
    <p class="weight">net wt. 2.5oz (70g)</p>
    <p class="site">www.lorvatique.com</p>
  </article>
  <article class="label scent-lagoon">
    <div class="wash" role="img" aria-label="Soft peach watercolour wash"></div>
    <div class="brand"><span class="brand-dot"></span><span class="brand-name">Lorvatique</span></div>
    <h2 class="product">VALDORA</h2>
    <p class="scent">Lagoon Infusion</p>
    <p class="scent-note">Exotic, mild scent with coconut and vanilla notes</p>
    <span class="divider"></span>
    <p class="claims">Naturally Refreshing<br>Baking Soda Free</p>
    <p class="weight">net wt. 2.5oz (70g)</p>
    <p class="site">www.lorvatique.com</p>
  </article>
  <article class="label scent-velvet">
    <div class="wash" role="img" aria-label="Soft golden watercolour wash"></div>
    <div class="brand"><span class="brand-dot"></span><span class="brand-name">Lorvatique</span></div>
    <h2 class="product">VALDORA</h2>
    <p class="scent">Velvet Grove</p>
    <p class="scent-note">Rich, woodsy scent with vanilla and sandalwood.</p>
    <span class="divider"></span>
    <p class="claims">Naturally Refreshing<br>Baking Soda Free</p>
    <p class="weight">net wt. 2.5oz (70g)</p>
    <p class="site">www.lorvatique.com</p>
  </article>

  <article class="label scent-unscented">
    <div class="wash" role="img" aria-label="Soft grey watercolour wash"></div>
    <div class="brand"><span class="brand-dot"></span><span class="brand-name">Lorvatique</span></div>
    <h2 class="product">VALDORA</h2>
    <p class="scent">Unscented</p>
    <p class="scent-note">A fragrance free option that still gives you the power of freshness all day</p>
    <span class="divider"></span>
    <p class="claims">Naturally Refreshing<br>Baking Soda Free</p>
    <p class="weight">net wt. 2.5oz (70g)</p>
    <p class="site">www.lorvatique.com</p>
  </article>
  <article class="label scent-amber">
    <div class="wash" role="img" aria-label="Soft teal watercolour wash"></div>
    <div class="brand"><span class="brand-dot"></span><span class="brand-name">Lorvatique</span></div>
    <h2 class="product">VALDORA</h2>
    <p class="scent">Amber Dusk</p>
    <p class="scent-note">Warm, exotic scent with amber and sandalwood notes</p>
    <span class="divider"></span>
    <p class="claims">Naturally Refreshing<br>Baking Soda Free</p>
    <p class="weight">net wt. 2.5oz (70g)</p>
    <p class="site">www.lorvatique.com</p>
  </article>
  <article class="label scent-meadow">
    <div class="wash" role="img" aria-label="Soft lavender watercolour wash"></div>
    <div class="brand"><span class="brand-dot"></span><span class="brand-name">Lorvatique</span></div>
    <h2 class="product">VALDORA</h2>
    <p class="scent">Calm Meadow</p>
    <p class="scent-note">Calm, refreshing scent with lavender notes</p>
    <span class="divider"></span>
    <p class="claims">Naturally Refreshing<br>Baking Soda Free</p>
    <p class="weight">net wt. 2.5oz (70g)</p>
    <p class="site">www.lorvatique.com</p>
  </article>

  <article class="label scent-orchard">
    <div class="wash" role="img" aria-label="Soft orange watercolour wash"></div>
    <div class="brand"><span class="brand-dot"></span><span class="brand-name">Lorvatique</span></div>
    <h2 class="product">VALDORA</h2>
    <p class="scent">Sunlit Orchard</p>
    <p class="scent-note">Light, breezy coconut scent with vanilla bean and mango notes</p>
    <span class="divider"></span>
    <p class="claims">Naturally Refreshing<br>Baking Soda Free</p>
    <p class="weight">net wt. 2.5oz (70g)</p>
    <p class="site">www.lorvatique.com</p>
  </article>
  <article class="label scent-garden">
    <div class="wash" role="img" aria-label="Soft blue watercolour wash"></div>
    <div class="brand"><span class="brand-dot"></span><span class="brand-name">Lorvatique</span></div>
    <h2 class="product">VALDORA</h2>
    <p class="scent">Garden Bloom</p>
    <p class="scent-note">Aromatic, green scent with rose, geranium and vanilla notes</p>
    <span class="divider"></span>
    <p class="claims">Naturally Refreshing<br>Baking Soda Free</p>
    <p class="weight">net wt. 2.5oz (70g)</p>
    <p class="site">www.lorvatique.com</p>
  </article>
  <article class="label label-back scent-unscented">
    <div class="wash" role="img" aria-label="Soft grey watercolour wash"></div>
    <div class="brand"><span class="brand-dot"></span><span class="brand-name">Lorvatique</span></div>
    <h2 class="product">VALDORA</h2>
    <p class="organic">100% ORGANIC</p>
    <p class="organic-sub">ALUMINUM FREE UNISEX DEODORANT</p>
    <p class="ingredients"><strong>Ingredients:</strong><br>Raw alkaline coconut oil, Mango butter, arrowroot powder, candelilla wax, zinc ricinoleate, zinc powder, vitamin E oil, fragrance</p>
    <div class="badges">
      <span class="badge">
        <svg viewBox="0 0 24 24" aria-hidden="true"><circle cx="12" cy="12" r="10.5" fill="none" stroke="#777" stroke-width="1.2"/><circle cx="12" cy="12" r="6" fill="none" stroke="#999" stroke-width="1"/></svg>
        CRUELTY FREE
      </span>
      <span class="badge">
        <svg viewBox="0 0 24 24" aria-hidden="true"><circle cx="12" cy="12" r="10.5" fill="none" stroke="#777" stroke-width="1.2"/><path d="M8 16 C8 10 12 7 17 7 C17 12 14 16 8 16 Z M8 16 L13 11" fill="none" stroke="#777" stroke-width="1.1"/></svg>
        VEGAN
      </span>
    </div>
    <p class="site">www.lorvatique.com</p>
  </article>
</section>

<p class="sheet-caption">BACK</p>

</body>
</html>
```